Master Slide Deck - Margin Loft

We need a Master Slide Deck that can used for all our internal and external presentations. CI should be aligned to the attached brand logo. We are open to your suggested fonts and pics. As we don't have a homepage yet, the fonts and pics should be also be applicable for the website. Please make a draft of some slides including pics. It should represent the company as a professional company who made its experience in sales and marketing.
Margin Loft is a company who has its goal to digitize expert knowledge (sales and marketing) into high-quality video episodes, enabling scalable and interactive knowledge transfer. Through digitalization, we can make expert knowledge more accessible, regardless of time and location, thus facilitating knowledge transfer and competency building for our target audience.

```html
<!DOCTYPE html>
<html lang="en">
<head>
<meta charset="utf-8">
<title>Margin Loft – Master Slide Deck</title>
<link href="https://fonts.googleapis.com/css2?family=Montserrat:wght@400;500;600;700;800&display=swap" rel="stylesheet">
<style>
:root{
  --navy:#0f3c78;
  --navy-dark:#0a2c5c;
  --grey:#9b9b9b;
  --grey-light:#d9d9d9;
  --text:#6b6b6b;
  --board:#808185;
  --white:#ffffff;
}
*{box-sizing:border-box;margin:0;padding:0}
html,body{width:904px;height:1200px;overflow:hidden}
body{background:var(--board);font-family:'Montserrat',sans-serif;position:relative}
.slide{position:absolute;width:515px;height:289px;background:var(--white);transform:scale(.5426);transform-origin:0 0;overflow:hidden;box-shadow:0 2px 6px rgba(0,0,0,.25)}
.slide > *{position:absolute}
.photo{background:linear-gradient(135deg,#c9d3e1,#8ea2bf 55%,#dfe5ee)}
.photo-dark{background:linear-gradient(120deg,#0f3c78 0%,#12447f 45%,#0b2f63 100%)}
.foot-brand{left:3px;bottom:8px;background:var(--navy);color:var(--white);font-size:10px;font-weight:700;padding:2px 6px;line-height:12px}
.page-num{right:12px;bottom:10px;font-size:8px;font-weight:700;color:var(--navy)}
.body{font-size:5.6px;line-height:7px;color:var(--text);text-align:justify}
.ttl{color:var(--navy);line-height:1;font-weight:500}
.ttl b{font-weight:800}
.item-h{font-size:11px;font-weight:600;color:var(--navy)}
.band{background:var(--white);border-radius:0 18px 0 0}
.band span{display:block;color:var(--navy);font-weight:800;line-height:1}
.over{color:var(--white);font-weight:400;letter-spacing:1px}
.sq{width:12px;height:12px;background:var(--navy);display:inline-block;margin-right:3px;border-radius:2px}
.brand-box{background:var(--navy);color:var(--white);font-weight:500;display:flex;align-items:center;padding-left:16px}
.dot{display:inline-block;width:6px;height:6px;border-radius:50%;background:var(--navy);margin-right:5px}
.dot.g{background:var(--grey)}
.legend{font-size:7.5px;font-weight:600;color:var(--navy)}
.legend p{font-size:4.5px;line-height:5.5px;color:var(--text);font-weight:400;margin-left:11px;width:90px}
.list{list-style:none;font-size:10.5px;line-height:18px;color:var(--text)}
.list li::before{content:"•";color:var(--navy);margin-right:6px}
.caption{font-size:10px;font-weight:600;color:var(--navy)}
.caption p{font-size:4.5px;line-height:5.5px;color:var(--text);font-weight:400}
.step-band{height:28px;display:flex;align-items:center;gap:6px;padding-left:5px;color:var(--white)}
.step-band.navy{background:var(--navy)}
.step-band.grey{background:#a7a7a7}
.step-band strong{font-size:11px;font-weight:800;padding-right:5px;border-right:1px solid rgba(255,255,255,.8);line-height:16px}
.step-band span{font-size:4px;line-height:5px;width:64px}
</style>
</head>
<body>

<!-- 01 Cover -->
<section class="slide cover" style="left:23px;top:23px">
  <div class="photo" role="img" aria-label="Photo of a smiling business team gathered around a laptop" style="left:250px;top:0;width:265px;height:289px;background:linear-gradient(90deg,#ffffff 0%,#d6dde8 25%,#9cafc8 60%,#e5e9ef 100%)"></div>
  <div class="brand-box" style="left:0;top:37px;width:235px;height:48px;font-size:29px">Margin Loft</div>
  <div style="left:415px;top:12px"><i class="sq"></i><i class="sq"></i><i class="sq"></i><i class="sq"></i></div>
  <div class="ttl" style="left:17px;top:155px;font-size:14px">PRESENTATION</div>
  <div class="ttl" style="left:16px;top:172px;font-size:34px;font-weight:800">BUSINESS</div>
  <div class="ttl" style="left:16px;top:210px;font-size:27px;font-weight:800">MARKETING</div>
  <div style="left:17px;top:247px;width:112px;height:3px;background:var(--navy)"></div>
  <div style="left:17px;top:260px;font-size:10px;letter-spacing:2px;font-weight:600;color:var(--navy)">www.marginloft.com</div>
</section>

<!-- 02 Contents -->
<section class="slide contents" style="left:312.5px;top:23px">
  <div class="ttl" style="left:30px;top:15px;font-size:25px;font-weight:800">Contents</div>
  <div style="left:30px;top:50px;width:72px;height:4px;background:var(--navy)"></div>
  <div style="left:52px;top:76px;width:440px;display:grid;grid-template-columns:1fr 1fr;row-gap:20px;column-gap:20px">
    <div><span class="item-h">1.&nbsp; Lorem ipsum</span><p class="body" style="margin-left:22px">Lorem ipsum dolor sit amet, consectetuer adipiscing elit, sed diam nonummy nibh euismod</p></div>
    <div><span class="item-h">2.&nbsp; Lorem ipsum</span><p class="body" style="margin-left:22px">Lorem ipsum dolor sit amet, consectetuer adipiscing elit, sed diam nonummy nibh euismod tincid</p></div>
    <div><span class="item-h">3.&nbsp; Lorem ipsum</span><p class="body" style="margin-left:22px">Lorem ipsum dolor sit amet, consectetuer adipiscing elit, sed diam nonummy nibh euismod</p></div>
    <div><span class="item-h">4.&nbsp; Lorem ipsum</span><p class="body" style="margin-left:22px">Lorem ipsum dolor sit amet, consectetuer adipiscing elit, sed diam nonummy nibh euismod tincid</p></div>
    <div><span class="item-h">5.&nbsp; Lorem ipsum</span><p class="body" style="margin-left:22px">Lorem ipsum dolor sit amet, consectetuer adipiscing elit, sed diam nonummy nibh euismod</p></div>
    <div><span class="item-h">6.&nbsp; Lorem ipsum</span><p class="body" style="margin-left:22px">Lorem ipsum dolor sit amet, consectetuer adipiscing elit, sed diam nonummy nibh euismod tincid</p></div>
  </div>
  <div class="foot-brand">Margin Loft</div><div class="page-num">02</div>
</section>

<!-- 03 About our company divider -->
<section class="slide divider" style="left:601px;top:23px">
  <div class="photo-dark" role="img" aria-label="Blue-toned photo of a businessman over a city skyline" style="left:0;top:0;width:515px;height:289px"></div>
  <div class="over" style="left:28px;top:92px;font-size:30px">ABOUT OUR</div>
  <div class="band" style="left:0;top:131px;width:300px;height:64px"><span style="font-size:52px;margin:6px 0 0 22px">COMPANY</span></div>
</section>

<!-- 04 About us -->
<section class="slide about" style="left:23px;top:190px">
  <div style="left:20px;top:27px;width:252px;height:225px;background:var(--navy);border-radius:0 30px 0 0;padding:14px 12px;color:var(--white)">
    <div style="font-size:17px;font-weight:600;line-height:1">ABOUT US</div>
    <div style="font-size:25px;font-weight:800;line-height:1.05">COMPANY</div>
    <p class="body" style="color:#e6ecf5;margin-top:10px">Lorem ipsum dolor sit amet, consectetuer adipiscing elit, sed diam nonummy nibh euismod tincidunt ut laoreet dolore magna aliquam erat volutpat. Ut wisi enim ad minim veniam, quis nostrud exerci tation ullamcorper suscipit lobortis nisl ut aliquip ex ea commodo consequat. Duis autem vel eum iriure dolor in hendrerit in vulputate velit esse molestie consequat, vel illum dolore eu feugiat nulla facilisis at vero eros et accumsan et iusto odio dignissim qui blandit praesent luptatum zzril delenit augue duis dolore te feugait nulla facilisi.</p>
    <p class="body" style="color:#e6ecf5;margin-top:8px">Lorem ipsum dolor sit amet, cons ectetuer adipiscing elit, sed diam nonummy nibh euismod tincidunt ut laoreet dolore magna aliquam erat volutpat. Ut wisi enim ad minim veniam, quis nostrud exerci tation ullamcorper suscipit lobortis nisl ut aliquip ex ea commodo consequat. Lorem ipsum dolor sit amet, consecac.</p>
  </div>
  <svg style="left:248px;top:48px" width="44" height="190" viewBox="0 0 44 190">
    <g fill="#fff" stroke="#0f3c78" stroke-width="3"><circle cx="22" cy="22" r="19"/><circle cx="22" cy="94" r="19"/><circle cx="22" cy="166" r="19"/></g>
    <g fill="none" stroke="#0f3c78" stroke-width="1.6"><rect x="13" y="15" width="18" height="12"/><path d="M16 24l4-4 3 3 5-5"/><path d="M14 94a5 5 0 0 1 5-5 6 6 0 0 1 11 2 4 4 0 0 1 0 8H16a3 3 0 0 1-2-5z"/><circle cx="14" cy="172" r="2.5"/><circle cx="22" cy="162" r="2.5"/><circle cx="30" cy="168" r="2.5"/><path d="M16 170l5-6M24 163l4 4"/></g>
  </svg>
  <div style="left:300px;top:52px;width:195px"><div class="item-h">Lorem ipsum</div><p class="body" style="font-size:6.4px;line-height:8px">ipsum dolor sit amet, cons ectetuer adipiscing elit, sed diam nonummy nibh euismod tincidunt ut laoreet</p></div>
  <div style="left:300px;top:122px;width:195px"><div class="item-h">Lorem ipsum</div><p class="body" style="font-size:6.4px;line-height:8px">ipsum dolor sit amet, cons ectetuer adipiscing elit, sed diam nonummy nibh euismod tincidunt ut laoreet dolore magna aliquam erat volutpat.</p></div>
  <div style="left:300px;top:196px;width:195px"><div class="item-h">Lorem ipsum</div><p class="body" style="font-size:6.4px;line-height:8px">ipsum dolor sit amet, cons ectetuer adipiscing elit, sed diam nonummy nibh euismod tincidunt</p></div>
  <div class="foot-brand">Margin Loft</div><div class="page-num">04</div>
</section>

<!-- 05 Education -->
<section class="slide education" style="left:312.5px;top:190px">
  <div class="ttl" style="left:15px;top:17px;font-size:18px">OUR COMPANY <b>EDUCATION</b></div>
  <div role="img" aria-label="Faint world map in the background" style="left:80px;top:48px;width:380px;height:175px;background:radial-gradient(ellipse at center,#eef1f5 0%,#f7f8fa 70%,#fff 100%)"></div>
  <svg style="left:90px;top:60px" width="340" height="150" viewBox="0 0 340 150">
    <g fill="#fff" stroke="#0f3c78" stroke-width="3"><rect x="5" y="8" width="95" height="138" rx="12"/><rect x="123" y="8" width="95" height="138" rx="12"/><rect x="243" y="8" width="95" height="138" rx="12"/></g>
    <g fill="#0f3c78"><circle cx="100" cy="60" r="5"/><circle cx="218" cy="60" r="5"/><circle cx="123" cy="100" r="5"/><circle cx="243" cy="100" r="5"/></g>
    <g fill="none" stroke="#0f3c78" stroke-width="1.4"><circle cx="52" cy="32" r="6"/><path d="M49 40h6"/><rect x="163" y="28" width="16" height="11"/><path d="M163 28l8 6 8-6"/><path d="M283 39h16M285 37l5-6 3 3 5-6"/></g>
  </svg>
  <div style="left:95px;top:114px;width:95px;text-align:center"><div class="caption" style="font-size:8px;font-weight:700">IDEA</div><p class="body" style="font-size:5px;line-height:6px;text-align:center;padding:3px 8px">Lorem ipsum dolor sit amet, consectetuer adipiscing elit, sed diam nonummy nibh euismod tincidunt ut laoreet dolore magna aliquam erat volutpat. Ut wisi enim ad minim veniam, quis nostrud exerci tation.</p></div>
  <div style="left:213px;top:114px;width:95px;text-align:center"><div class="caption" style="font-size:8px;font-weight:700">PROMOTION</div><p class="body" style="font-size:5px;line-height:6px;text-align:center;padding:3px 8px">Lorem ipsum dolor sit amet, consectetuer adipiscing elit, sed diam nonummy nibh euismod tincidunt ut laoreet dolore magna aliquam erat volutpat. Ut wisi enim ad minim veniam, quis nostrud exerci tation.</p></div>
  <div style="left:333px;top:114px;width:95px;text-align:center"><div class="caption" style="font-size:8px;font-weight:700">GROWTH</div><p class="body" style="font-size:5px;line-height:6px;text-align:center;padding:3px 8px">Lorem ipsum dolor sit amet, consectetuer adipiscing elit, sed diam nonummy nibh euismod tincidunt ut laoreet dolore magna aliquam erat volutpat. Ut wisi enim ad minim veniam, quis nostrud exerci tation.</p></div>
  <div style="left:62px;top:228px;width:410px;border:1px solid var(--grey);padding:2px 6px"><p class="body" style="text-align:center;color:#333">Lorem ipsum dolor sit amet, consectetuer adipiscing elit, sed diam nonummy nibh euismod tincidunt ut laoreet dolore magna aliquam erat volutpat. Ut wisi enim ad minim veniam, quis nostrud exerci tation ullamcorper suscipit lobortis nisl ut aliquip ex ea commodo consequat. Duis autem vel eum iriure dolor in hendrerit.</p></div>
  <div class="foot-brand">Margin Loft</div><div class="page-num">05</div>
</section>

<!-- 06 Market -->
<section class="slide market" style="left:601px;top:190px">
  <div class="ttl" style="left:20px;top:27px;font-size:19px;font-weight:800">MARKET<br>OPPORTUNITIES</div>
  <p class="body" style="left:20px;top:72px;width:202px;font-size:5px;line-height:6px">Lorem ipsum dolor sit amet, consectetuer adipiscing elit, sed diam nonummy nibh euismod tincidunt ut laoreet dolore magna aliquam erat volutpat. Ut wisi enim ad minim veniam, quis nostrud exerci tation ullamcorper suscipit lobortis nisl ut aliquip ex ea commodo consequat. Duis autem vel eum iriure dolor in hendrerit.</p>
  <p class="body" style="left:20px;top:112px;width:202px;font-size:5px;line-height:6px">Lorem ipsum dolor sit amet, consectetuer adipiscing elit, sed diam nonummy.</p>
  <svg style="left:25px;top:140px" width="170" height="110" viewBox="0 0 170 110">
    <g transform="translate(85 55)">
      <path d="M0-38A70 38 0 0 1 70 0L30 0A30 14 0 0 0 0-14Z" fill="#a7a7a7"/>
      <path d="M70 0A70 38 0 0 1 0 38L0 14A30 14 0 0 0 30 0Z" fill="#0f3c78"/>
      <path d="M0 38A70 38 0 0 1-70 0L-30 0A30 14 0 0 0 0 14Z" fill="#a7a7a7"/>
      <path d="M-70 0A70 38 0 0 1 0-38L0-14A30 14 0 0 0-30 0Z" fill="#0f3c78"/>
      <path d="M-70 0v14A70 38 0 0 0 0 52V38A70 38 0 0 1-70 0Z" fill="#0a2c5c"/>
      <path d="M0 38v14A70 38 0 0 0 70 14V0A70 38 0 0 1 0 38Z" fill="#7e7e7e"/>
      <g font-family="Montserrat,sans-serif" font-weight="700" font-size="11" fill="#fff"><text x="-5" y="-20">20%</text><text x="35" y="6">20%</text><text x="-5" y="30">20%</text><text x="-62" y="8">40%</text></g>
    </g>
  </svg>
  <div style="left:245px;top:37px;font-size:7.5px;font-weight:700;color:#222">CONSECTETUER ADIPISCING</div>
  <svg style="left:232px;top:52px" width="270" height="145" viewBox="0 0 270 145" font-family="Montserrat,sans-serif" font-size="7" fill="#555">
    <g stroke="#ddd" stroke-width=".8"><line x1="22" y1="8" x2="262" y2="8"/><line x1="22" y1="26" x2="262" y2="26"/><line x1="22" y1="44" x2="262" y2="44"/><line x1="22" y1="62" x2="262" y2="62"/><line x1="22" y1="80" x2="262" y2="80"/><line x1="22" y1="98" x2="262" y2="98"/><line x1="262" y1="8" x2="262" y2="116"/></g>
    <line x1="22" y1="116" x2="262" y2="116" stroke="#555"/>
    <g text-anchor="end"><text x="16" y="10">60</text><text x="16" y="28">50</text><text x="16" y="46">40</text><text x="16" y="64">30</text><text x="16" y="82">20</text><text x="16" y="100">10</text><text x="16" y="118">0</text></g>
    <rect x="38" y="17" width="25" height="99" fill="#0f3c78"/><rect x="94" y="84" width="25" height="32" fill="#a7a7a7"/><rect x="150" y="31" width="25" height="85" fill="#0f3c78"/><rect x="206" y="67" width="25" height="49" fill="#a7a7a7"/>
    <g text-anchor="middle"><text x="50" y="130">JAN</text><text x="106" y="130">FEB</text><text x="162" y="130">MAR</text><text x="218" y="130">APR</text></g>
  </svg>
  <div class="legend" style="left:245px;top:204px"><i class="dot"></i>Lorem ipsum<p>Lorem ipsum dolor sit amet, consectetuer adipiscing elit, sed diam nonummy nibh euismod tincidunt ut laoreet</p></div>
  <div class="legend" style="left:370px;top:204px"><i class="dot"></i>Lorem ipsum<p>Lorem ipsum dolor sit amet, consectetuer adipiscing elit, sed diam nonummy nibh euismod tincidunt ut laoreet</p></div>
  <div class="foot-brand">Margin Loft</div><div class="page-num">06</div>
</section>

<!-- 07 Overview -->
<section class="slide overview" style="left:23px;top:356.5px">
  <div class="ttl" style="left:20px;top:22px;font-size:16px">COMPANY<br><b style="font-size:25px">OVERVIEW</b></div>
  <p class="body" style="left:20px;top:68px;width:210px;font-size:5px;line-height:6px">Lorem ipsum dolor sit amet, consectetuer adipiscing elit, sed diam nonummy nibh euismod tincidunt ut laoreet dolore magna aliquam erat volutpat. Ut wisi enim ad minim veniam, quis nostrud exerci tation ullamcorper suscipit lobortis nisl ut aliquip ex ea commodo consequat. Duis autem vel eum iriure dolor in hendrerit</p>
  <p class="body" style="left:20px;top:113px;width:210px;font-size:5px;line-height:6px">erat volutpat. Ut wisi enim ad minim veniam, quis nostrud exerci tation ullamcorper suscipit lobortis nisl ut aliquip ex ea commodo consequat. Duis autem vel eum iriure dolor in hendrerit</p>
  <svg style="left:245px;top:22px" width="260" height="135" viewBox="0 0 260 135" font-family="Montserrat,sans-serif" font-size="7" fill="#555">
    <g stroke="#ddd" stroke-width=".8"><line x1="22" y1="8" x2="255" y2="8"/><line x1="22" y1="26" x2="255" y2="26"/><line x1="22" y1="44" x2="255" y2="44"/><line x1="22" y1="62" x2="255" y2="62"/><line x1="22" y1="80" x2="255" y2="80"/><line x1="22" y1="98" x2="255" y2="98"/><line x1="255" y1="8" x2="255" y2="116"/></g>
    <line x1="22" y1="116" x2="255" y2="116" stroke="#555"/>
    <g text-anchor="end"><text x="16" y="10">60</text><text x="16" y="28">50</text><text x="16" y="46">40</text><text x="16" y="64">30</text><text x="16" y="82">20</text><text x="16" y="100">10</text><text x="16" y="118">0</text></g>
    <rect x="40" y="44" width="7" height="72" fill="#a7a7a7"/><rect x="50" y="31" width="7" height="85" fill="#0f3c78"/>
    <rect x="96" y="98" width="7" height="18" fill="#a7a7a7"/><rect x="106" y="53" width="7" height="63" fill="#0f3c78"/>
    <rect x="152" y="14" width="7" height="102" fill="#0f3c78"/><rect x="162" y="76" width="7" height="40" fill="#a7a7a7"/>
    <rect x="208" y="28" width="7" height="88" fill="#0f3c78"/><rect x="218" y="62" width="7" height="54" fill="#a7a7a7"/>
    <g text-anchor="middle"><text x="50" y="128">JAN</text><text x="105" y="128">FEB</text><text x="161" y="128">MAR</text><text x="217" y="128">APR</text></g>
  </svg>
  <svg style="left:15px;top:150px" width="240" height="100" viewBox="0 0 240 100" font-family="Montserrat,sans-serif" font-size="6" fill="#555">
    <g stroke="#e3e3e3" stroke-width=".6"><line x1="18" y1="10" x2="235" y2="10"/><line x1="18" y1="22" x2="235" y2="22"/><line x1="18" y1="34" x2="235" y2="34"/><line x1="18" y1="46" x2="235" y2="46"/><line x1="18" y1="58" x2="235" y2="58"/><line x1="18" y1="70" x2="235" y2="70"/></g>
    <line x1="18" y1="82" x2="235" y2="82" stroke="#555" stroke-width=".6"/>
    <g text-anchor="end"><text x="13" y="12">60</text><text x="13" y="24">50</text><text x="13" y="36">40</text><text x="13" y="48">30</text><text x="13" y="60">20</text><text x="13" y="72">10</text><text x="13" y="84">0</text></g>
    <polyline points="30,82 52,70 74,48 96,60 118,56 140,60 162,58 184,50 206,40" fill="none" stroke="#a7a7a7" stroke-width="1.2"/>
    <polyline points="30,64 52,76 74,54 96,22 118,30 140,52 162,44 184,34 206,68" fill="none" stroke="#0f3c78" stroke-width="1.4"/>
    <g fill="#0f3c78"><circle cx="30" cy="64" r="1.8"/><circle cx="52" cy="76" r="1.8"/><circle cx="74" cy="54" r="1.8"/><circle cx="96" cy="22" r="1.8"/><circle cx="118" cy="30" r="1.8"/><circle cx="140" cy="52" r="1.8"/><circle cx="162" cy="44" r="1.8"/><circle cx="184" cy="34" r="1.8"/><circle cx="206" cy="68" r="1.8"/></g>
    <g font-size="4.5" text-anchor="middle"><text x="30" y="90">TEXT 01</text><text x="52" y="90">TEXT 02</text><text x="74" y="90">TEXT 03</text><text x="96" y="90">TEXT 04</text><text x="118" y="90">TEXT 05</text><text x="140" y="90">TEXT 06</text><text x="162" y="90">TEXT 07</text><text x="184" y="90">TEXT 08</text><text x="206" y="90">TEXT 09</text></g>
  </svg>
  <div class="legend" style="left:268px;top:170px"><i class="dot"></i>Lorem ipsum<p>Lorem ipsum dolor sit amet, consectetuer adipiscing elit, sed diam nonummy nibh euismod tincidunt</p></div>
  <div class="legend" style="left:388px;top:170px"><i class="dot"></i>Lorem ipsum<p>Lorem ipsum dolor sit amet, consectetuer adipiscing elit, sed diam nonummy nibh euismod tincidunt</p></div>
  <div class="legend" style="left:268px;top:210px"><i class="dot"></i>Lorem ipsum<p>Lorem ipsum dolor sit amet, consectetuer adipiscing elit, sed diam nonummy nibh euismod tincidunt</p></div>
  <div class="legend" style="left:388px;top:210px"><i class="dot"></i>Lorem ipsum<p>Lorem ipsum dolor sit amet, consectetuer adipiscing elit, sed diam nonummy nibh euismod tincidunt</p></div>
  <div class="foot-brand">Margin Loft</div><div class="page-num">07</div>
</section>

<!-- 08 About our service divider -->
<section class="slide divider" style="left:312.5px;top:356.5px">
  <div class="photo-dark" role="img" aria-label="Blue-toned photo of a businessman on the phone over a city skyline" style="left:0;top:0;width:515px;height:289px"></div>
  <div class="over" style="left:28px;top:88px;font-size:30px">ABOUT OUR</div>
  <div class="band" style="left:0;top:127px;width:300px;height:64px"><span style="font-size:54px;margin:4px 0 0 22px">SERVICE</span></div>
</section>

<!-- 09 Domain -->
<section class="slide domain" style="left:601px;top:356.5px">
  <div style="left:0;top:0;width:82px;height:35px;background:var(--navy)"></div>
  <div class="photo" role="img" aria-label="Photo of two colleagues smiling at a meeting table with charts" style="left:28px;top:38px;width:215px;height:205px;border:3px solid #fff"></div>
  <div class="ttl" style="left:267px;top:37px;font-size:13.5px;line-height:19px">WHAT'S A DOMAIN?<br>IT'S THAT NAME UP<br><b>IN THE ADDRESS BAR.</b></div>
  <ul class="list" style="left:267px;top:104px">
    <li>Fits your business or products</li><li>Is easy to spell and remember</li><li>Fits your business or products</li><li>Is easy to spell and remember</li><li>Fits your business or products</li><li>Is easy to spell and remember</li><li>Fits your business or products</li>
  </ul>
  <div class="foot-brand">Margin Loft</div><div class="page-num">09</div>
</section>

<!-- 10 Active intelligence -->
<section class="slide intelligence" style="left:23px;top:522.5px">
  <div style="left:30px;top:33px;width:158px;height:3px;background:var(--navy)"></div>
  <div class="photo" role="img" aria-label="Photo of a team working with laptops in a bright office" style="left:0;top:42px;width:272px;height:190px"></div>
  <div style="left:276px;top:150px;width:3px;height:92px;background:var(--navy)"></div>
  <div class="ttl" style="left:288px;top:32px;font-size:17px">ACTIVE<br><b>INTELLIGENCE</b></div>
  <p class="body" style="left:288px;top:74px;width:207px">Lorem ipsum dolor sit amet, consectetuer adipiscing elit, sed diam nonummy nibh euismod tincidunt ut laoreet dolore magna aliquam erat volutpat. Ut wisi enim ad minim veniam, quis nostrud exerci tation ullamcorper suscipit lobortis nisl ut aliquip ex ea commodo consequat. Duis autem vel eum iriure dolor in hendrerit in vulputate velit esse</p>
  <p class="body" style="left:288px;top:124px;width:207px">Lorem ipsum dolor sit amet, consectetuer adipiscing elit, sed diam nonummy nibh euismod tincidunt ut laoreet dolore magna aliquam erat volutpat. Ut wisi enim ad minim veniam, quis nostrud exerci tation ullamcorper suscipit lobortis nisl ut aliquip ex ea commodo consequat. Duis autem vel eum iriure dolor in hendrerit in vulputate velit esse</p>
  <p class="body" style="left:288px;top:185px;width:207px;font-size:5px">▶&nbsp; Lorem ipsum dolor sit amet, consectetuer adipiscing elit, sed diam nonummy nibh euismod tincidunt ut laoreet dolore magna</p>
  <p class="body" style="left:288px;top:207px;width:207px;font-size:5px">▷&nbsp; Lorem ipsum dolor sit amet, consectetuer adipiscing elit, sed diam nonummy nibh euismod tincidunt ut laoreet dolore magna</p>
  <div class="foot-brand">Margin Loft</div><div class="page-num">10</div>
</section>

<!-- 11 Options diagram -->
<section class="slide options" style="left:312.5px;top:522.5px">
  <div class="ttl" style="left:17px;top:12px;font-size:17px">LOREM IPSUM <b>DOLOR SIT AMET</b></div>
  <svg style="left:0;top:0" width="515" height="289" viewBox="0 0 515 289" font-family="Montserrat,sans-serif">
    <g fill="none" stroke="#0f3c78" stroke-width="3">
      <path d="M215 122 L235 148 M289 122 L268 148 M180 160 L215 170 M322 160 L288 170"/>
    </g>
    <g fill="#fff" stroke="#0f3c78" stroke-width="3">
      <circle cx="207" cy="100" r="28"/><circle cx="296" cy="100" r="28"/><circle cx="158" cy="152" r="28"/><circle cx="345" cy="152" r="28"/>
    </g>
    <circle cx="252" cy="178" r="42" fill="#fff" stroke="#0f3c78" stroke-width="6" stroke-dasharray="10 4"/>
    <circle cx="252" cy="178" r="30" fill="#fff" stroke="#0f3c78" stroke-width="2"/>
    <text x="252" y="181" text-anchor="middle" font-size="7" font-weight="700" fill="#0f3c78">Margin Loft</text>
    <g font-size="6" font-weight="600" fill="#8a9bb5" text-anchor="middle"><text x="207" y="112">Option B</text><text x="296" y="112">Option C</text><text x="158" y="164">Option A</text><text x="345" y="164">Option D</text></g>
    <g fill="none" stroke="#0f3c78" stroke-width="1.5"><rect x="201" y="88" width="12" height="9"/><path d="M290 92h12l-2 6h-8z"/><path d="M151 144l7-4 7 4-7 4z"/><rect x="339" y="142" width="12" height="9"/></g>
    <g font-size="8" font-weight="700" fill="#0f3c78"><text x="128" y="71">Your Title</text><text x="325" y="64">Your Title</text><text x="79" y="135">Your Title</text><text x="375" y="133">Your Title</text></g>
    <g font-size="4.5" fill="#666"><text x="118" y="79">Lorem ipsum dolor sit amet,</text><text x="118" y="85">adipiscing elit, sed diam</text><text x="325" y="72">Lorem ipsum dolor sit</text><text x="325" y="78">amet, adipiscing elit</text><text x="72" y="143">Lorem ipsum dolor sit</text><text x="72" y="149">amet, sed diam nonummy</text><text x="375" y="141">Lorem ipsum dolor sit</text><text x="375" y="147">amet, sed diam nonummy</text></g>
  </svg>
  <p class="body" style="left:55px;top:230px;width:410px;text-align:center;color:#333">Lorem ipsum dolor sit amet, consectetuer adipiscing elit, sed diam nonummy nibh euismod tincidunt ut laoreet dolore magna aliquam erat volutpat. Ut wisi enim ad minim veniam, quis nostrud exerci tation ullamcorper suscipit lobortis nisl ut aliquip ex ea commodo consequat. Duis autem vel eum iriure dolor in hendrerit</p>
  <div class="foot-brand">Margin Loft</div><div class="page-num">11</div>
</section>

<!-- 12 Benefits -->
<section class="slide benefits" style="left:601px;top:522.5px">
  <div class="ttl" style="left:22px;top:22px;font-size:17px;line-height:20px">BENEFITS TO EACH<br><b>CUSTOMER SEGMENTS</b></div>
  <div style="left:22px;top:72px;width:236px;display:flex;flex-direction:column;gap:6px">
    <p class="body">Lorem ipsum dolor sit amet, consectetuer adipiscing elit, sed diam nonummy nibh euismod tincidunt ut laoreet dolore magna aliquam erat volutpat. Ut wisi enim ad minim veniam, quis nostrud exerci tation ullam</p>
    <p class="body">Lorem ipsum dolor sit amet, consectetuer adipiscing elit, sed diam nonummy nibh euismod tincidunt ut laoreet dolore magna aliquam erat volutpat. Ut wisi enim ad minim veniam, quis nostrud exerci tation ullam</p>
    <p class="body">Lorem ipsum dolor sit amet, consectetuer adipiscing elit, sed diam nonummy nibh euismod tincidunt ut laoreet dolore magna aliquam erat volutpat. Ut wisi enim ad minim veniam, quis nostrud exerci</p>
    <p class="body">Lorem ipsum dolor sit amet, consectetuer adipiscing elit, sed diam nonummy nibh euismod tincidunt ut laoreet dolore magna aliquam erat volutpat. Ut wisi enim ad minim veniam, quis nostrud exerci tation ullam</p>
    <p class="body">Lorem ipsum dolor sit amet, consectetuer adipiscing elit, sed diam nonummy nibh euismod tincidunt ut laoreet dolore magna aliquam erat volutpat. Ut wisi enim ad minim veniam, quis nostrud exerci</p>
  </div>
  <div style="left:287px;top:38px;width:26px;height:26px;background:var(--navy)"></div>
  <div class="photo" role="img" aria-label="Photo of a presenter beside a whiteboard with sticky notes and charts" style="left:295px;top:50px;width:200px;height:190px;background:linear-gradient(135deg,#eef0f2,#cfd6df 55%,#b9c2cd)"></div>
  <div class="foot-brand">Margin Loft</div><div class="page-num">12</div>
</section>

<!-- 13 About our project divider -->
<section class="slide divider" style="left:23px;top:688px">
  <div class="photo-dark" role="img" aria-label="Blue-toned photo of a businessman over a city skyline" style="left:0;top:0;width:515px;height:289px"></div>
  <div class="over" style="left:28px;top:88px;font-size:30px">ABOUT OUR</div>
  <div class="band" style="left:0;top:128px;width:300px;height:64px"><span style="font-size:54px;margin:4px 0 0 22px">PROJECT</span></div>
</section>

<!-- 14 Project -->
<section class="slide project" style="left:312.5px;top:688px">
  <div class="ttl" style="left:0;top:25px;width:515px;text-align:center;font-size:18px">LOREM IPSUM <b>PROJECT</b></div>
  <p class="body" style="left:80px;top:50px;width:355px;text-align:center">Lorem ipsum dolor sit amet, consectetuer adipiscing elit, sed diam nonummy nibh euismod tincidunt ut laoreet dolore magna aliquam erat volutpat. Ut wisi enim ad minim veniam, quis nostrud exerci tation ullamcorper suscipit lobortis nisl utea commodo consequat. Duis autem vel eum iriure dolor in hendrerit</p>
  <p class="body" style="left:80px;top:82px;width:355px;text-align:center">Lorem ipsum dolor sit amet, consectetuer adipiscing elit, sed diam nonummy nibh m ipsum dolor sit amet, consectetuer adipiscing elit, sed diam nonummy nibh euismod tincidunt ut laoreet dolore magna.</p>
  <div class="photo" role="img" aria-label="Photo of a hand touching a glowing interface" style="left:20px;top:120px;width:112px;height:80px;border:2px solid #d0d6de;background:linear-gradient(135deg,#1b3f73,#6b8fbf)"></div>
  <div class="photo" role="img" aria-label="Photo of business people at a meeting table" style="left:141px;top:120px;width:112px;height:80px;border:2px solid #d0d6de"></div>
  <div class="photo" role="img" aria-label="Photo of a digital network interface in blue" style="left:262px;top:120px;width:112px;height:80px;border:2px solid #d0d6de;background:linear-gradient(135deg,#0b2f63,#2d6ab8)"></div>
  <div class="photo" role="img" aria-label="Photo of a hand over agile process icons" style="left:383px;top:120px;width:112px;height:80px;border:2px solid #d0d6de;background:linear-gradient(135deg,#2a4a6a,#7ea3c4)"></div>
  <div class="caption" style="left:20px;top:205px;width:112px">Lorem ipsum<p>Lorem ipsum dolor sit amet, consectetuer adipiscing elit, sed diam nonummy nibh euismod tincidunt ut laoreet</p></div>
  <div class="caption" style="left:141px;top:205px;width:112px">Lorem ipsum<p>Lorem ipsum dolor sit amet, consectetuer adipiscing elit, sed diam nonummy nibh euismod tincidunt ut laoreet</p></div>
  <div class="caption" style="left:262px;top:205px;width:112px">Lorem ipsum<p>Lorem ipsum dolor sit amet, consectetuer adipiscing elit, sed diam nonummy nibh euismod tincidunt ut laoreet</p></div>
  <div class="caption" style="left:383px;top:205px;width:112px">Lorem ipsum<p>Lorem ipsum dolor sit amet, consectetuer adipiscing elit, sed diam nonummy nibh euismod tincidunt ut laoreet</p></div>
  <div class="foot-brand">Margin Loft</div><div class="page-num">14</div>
</section>

<!-- 15 Portfolio -->
<section class="slide portfolio" style="left:601px;top:688px">
  <div class="photo" role="img" aria-label="Photo of hands typing on a laptop showing a marketing chart" style="left:22px;top:42px;width:200px;height:215px;border:3px solid #fff;outline:1px solid #c8ced6;background:linear-gradient(135deg,#e3e6ea,#a9b4c2 55%,#4b5b70)"></div>
  <div class="ttl" style="left:237px;top:36px;font-size:12px">PORTFOLIO OF<br><b style="font-size:26px;line-height:32px">PROJECTS</b></div>
  <p class="body" style="left:237px;top:88px;width:262px">Lorem ipsum dolor sit amet, consectetuer adipiscing elit, sed diam nonummy nibh euismod tincidunt ut laoreet dolore magna aliquam erat volutpat. Ut wisi enim ad minim veniam, quis nostrud exerci tation ullamcorper suscipit lobortis nisl ut aliquip ex ea commodo consequat. Duis autem vel eum iriure dolor in hendrerit in vulputate velit esse</p>
  <p class="body" style="left:237px;top:135px;width:262px">Lorem ipsum dolor sit amet, consectetuer adipiscing elit, sed diam nonummy nibh euismod tincidunt ut laoreet dolore magna aliquam erat volutpat. Ut wisi enim ad minim veniam, quis nostrud exerci tation ullamcorper suscipit lobortis nisl ut aliquip ex ea commodo consequat. Duis autem vel eum iriure dolor in hendrerit in vulputate velit esse</p>
  <p class="body" style="left:237px;top:186px;width:262px;font-size:5px">▶&nbsp; Lorem ipsum dolor sit amet, consectetuer adipiscing elit, sed diam nonummy nibh euismod tincidunt ut laoreet dolore magna</p>
  <p class="body" style="left:237px;top:218px;width:262px;font-size:5px">▷&nbsp; Lorem ipsum dolor sit amet, consectetuer adipiscing elit, sed diam nonummy nibh euismod tincidunt ut laoreet dolore magna</p>
  <div class="foot-brand">Margin Loft</div><div class="page-num">15</div>
</section>

<!-- 16 Roadmap -->
<section class="slide roadmap" style="left:23px;top:854px">
  <svg style="left:0;top:0" width="515" height="289" viewBox="0 0 515 289" font-family="Montserrat,sans-serif">
    <path d="M458 225 L458 175 M455 225 Q450 230 320 225 Q250 220 250 180 Q250 160 300 150 Q355 135 330 118 Q300 105 270 95 Q240 80 260 55 M200 70 Q215 45 240 45" fill="none" stroke="#0f3c78" stroke-width="2"/>
    <path d="M270 95 L270 105 M330 118 L330 130" stroke="#0f3c78" stroke-width="1.4" stroke-dasharray="2 3"/>
    <g fill="#fff" stroke="#0f3c78">
      <circle cx="455" cy="130" r="36" stroke-width="5"/><circle cx="455" cy="130" r="28" stroke-width="1.5"/>
      <circle cx="267" cy="95" r="18" stroke-width="3.5"/>
      <circle cx="352" cy="62" r="15" stroke-width="3"/>
      <circle cx="198" cy="62" r="11" stroke-width="2.5"/>
      <circle cx="240" cy="35" r="8" stroke-width="2"/>
      <circle cx="163" cy="35" r="6" stroke-width="1.6"/>
    </g>
    <g fill="#0f3c78" font-weight="700" text-anchor="middle"><text x="455" y="146" font-size="44">1</text><text x="267" y="103" font-size="22">2</text><text x="352" y="69" font-size="18">3</text><text x="198" y="67" font-size="13">4</text><text x="240" y="39" font-size="10">5</text><text x="163" y="38" font-size="7">6</text></g>
    <g fill="#0f3c78" font-size="8" font-weight="700"><text x="88" y="41">Lorem Ipsum</text><text x="258" y="27">Lorem Ipsum</text><text x="378" y="35">Lorem Ipsum</text><text x="182" y="112">Lorem Ipsum</text><text x="357" y="150">Lorem Ipsum</text></g>
    <g fill="#666" font-size="4.5"><text x="88" y="48">Lorem ipsum dolor sit amet,</text><text x="88" y="54">adipiscing elit, sed diam</text><text x="258" y="34">Lorem ipsum dolor sit amet,</text><text x="258" y="40">adipiscing elit, sed diam</text><text x="378" y="42">Lorem ipsum dolor sit amet,</text><text x="378" y="48">adipiscing elit, sed diam</text><text x="182" y="119">Lorem ipsum dolor sit amet,</text><text x="182" y="125">adipiscing elit, sed diam</text><text x="357" y="157">Lorem ipsum dolor sit amet,</text><text x="357" y="163">adipiscing elit, sed diam</text></g>
    <circle cx="45" cy="225" r="13" fill="#0f3c78"/><text x="45" y="230" text-anchor="middle" fill="#fff" font-size="14" font-weight="700">A</text>
    <circle cx="145" cy="225" r="13" fill="#0f3c78"/><text x="145" y="230" text-anchor="middle" fill="#fff" font-size="14" font-weight="700">B</text>
    <g fill="#0f3c78" font-size="13" font-weight="600"><text x="62" y="218">2019</text><text x="162" y="218">2020</text></g>
    <g fill="#666" font-size="4.5"><text x="62" y="228">Lorem ipsum dolor sit</text><text x="62" y="234">amet, adipiscing elit</text><text x="162" y="228">Lorem ipsum dolor sit</text><text x="162" y="234">amet, sed diam</text></g>
  </svg>
  <div class="ttl" style="left:22px;top:128px;font-size:10.5px;letter-spacing:1.5px">TIMELINE OF</div>
  <div class="ttl" style="left:21px;top:142px;font-size:24px;font-weight:800">ROADMAP</div>
  <div class="ttl" style="left:24px;top:168px;font-size:12px;font-weight:700">FOR 2 YEARS</div>
  <div class="foot-brand">Margin Loft</div><div class="page-num">16</div>
</section>

<!-- 17 Timeline -->
<section class="slide timeline" style="left:312.5px;top:854px">
  <div class="ttl" style="left:17px;top:12px;font-size:13px">TIMELINE &nbsp;<b style="font-size:24px">INFOGRAPHIC</b></div>
  <svg style="left:0;top:0" width="515" height="289" viewBox="0 0 515 289" font-family="Montserrat,sans-serif">
    <line x1="75" y1="152" x2="475" y2="152" stroke="#0f3c78" stroke-width="1"/>
    <g fill="none" stroke="#9b9b9b" stroke-width="2.5">
      <path d="M100 152V100a12 12 0 0 1 12-12h33a12 12 0 0 1 12 12v52"/>
      <path d="M240 152V100a12 12 0 0 1 12-12h33a12 12 0 0 1 12 12v52"/>
      <path d="M382 152V100a12 12 0 0 1 12-12h33a12 12 0 0 1 12 12v52"/>
      <path d="M170 152v52a12 12 0 0 0 12 12h33a12 12 0 0 0 12-12v-52"/>
      <path d="M311 152v52a12 12 0 0 0 12 12h33a12 12 0 0 0 12-12v-52"/>
    </g>
    <g fill="#fff" stroke="#0f3c78" stroke-width="3"><circle cx="128" cy="88" r="11"/><circle cx="268" cy="88" r="11"/><circle cx="410" cy="88" r="11"/><circle cx="198" cy="216" r="11"/><circle cx="339" cy="216" r="11"/></g>
    <g fill="#0f3c78"><circle cx="128" cy="88" r="6"/><circle cx="268" cy="88" r="6"/><circle cx="410" cy="88" r="6"/><circle cx="198" cy="216" r="6"/><circle cx="339" cy="216" r="6"/></g>
    <g fill="#0f3c78" font-size="17" font-weight="500" text-anchor="middle"><text x="128" y="135">2018</text><text x="268" y="135">2020</text><text x="410" y="135">2022</text><text x="198" y="182">2019</text><text x="339" y="182">2021</text></g>
    <g fill="#0f3c78" font-size="5.5" font-weight="700" text-anchor="middle"><text x="198" y="80">LOREM IPSUM</text><text x="339" y="80">LOREM IPSUM</text><text x="128" y="180">LOREM IPSUM</text><text x="268" y="180">LOREM IPSUM</text><text x="410" y="180">LOREM IPSUM</text></g>
    <g fill="#0f3c78"><rect x="193" y="62" width="3" height="8"/><rect x="197" y="58" width="3" height="12"/><rect x="201" y="54" width="3" height="16"/><path d="M333 68l10-12 2 6z"/><circle cx="128" cy="168" r="3"/><circle cx="268" cy="168" r="3.5"/><rect x="405" y="166" width="9" height="5"/></g>
    <g fill="#666" font-size="5" text-anchor="middle">
      <text x="198" y="90">Lorem ipsum</text><text x="198" y="97">dolor sit amet,</text><text x="198" y="104">consectetur</text><text x="198" y="111">adipiscing elit.</text><text x="198" y="118">Duis elit sapien,</text><text x="198" y="125">sit amet, egestas</text><text x="198" y="132">commodo arcu.</text>
      <text x="339" y="90">Lorem ipsum</text><text x="339" y="97">dolor sit amet,</text><text x="339" y="104">consectetur</text><text x="339" y="111">adipiscing elit.</text><text x="339" y="118">Duis elit sapien,</text><text x="339" y="125">sit amet, egestas</text><text x="339" y="132">commodo arcu.</text>
      <text x="128" y="190">Lorem ipsum</text><text x="128" y="197">dolor sit amet,</text><text x="128" y="204">consectetur</text><text x="128" y="211">adipiscing elit.</text><text x="128" y="218">Duis elit sapien,</text><text x="128" y="225">sit amet, egestas</text><text x="128" y="232">commodo arcu.</text>
      <text x="268" y="190">Lorem ipsum</text><text x="268" y="197">dolor sit amet,</text><text x="268" y="204">consectetur</text><text x="268" y="211">adipiscing elit.</text><text x="268" y="218">Duis elit sapien,</text><text x="268" y="225">sit amet, egestas</text><text x="268" y="232">commodo arcu.</text>
      <text x="410" y="190">Lorem ipsum</text><text x="410" y="197">dolor sit amet,</text><text x="410" y="204">consectetur</text><text x="410" y="211">adipiscing elit.</text><text x="410" y="218">Duis elit sapien,</text><text x="410" y="225">sit amet, egestas</text><text x="410" y="232">commodo arcu.</text>
    </g>
  </svg>
  <div class="foot-brand">Margin Loft</div><div class="page-num">17</div>
</section>

<!-- 18 Steps -->
<section class="slide steps" style="left:601px;top:854px">
  <div class="ttl" style="left:18px;top:18px;font-size:17px;line-height:20px">STARTING<br><b>LOREM IPSUM</b></div>
  <div role="img" aria-label="Illustration of rising steps topped by an upward arrow" style="left:222px;top:12px;width:112px;height:225px;background:linear-gradient(180deg,#0f3c78 0%,#2c5590 55%,#a7a7a7 100%)"></div>
  <div class="step-band navy" style="left:126px;top:82px;width:96px"><strong>50%</strong><span>Lorem ipsum dolor sit amet, adipiscing elit, sed diam</span></div>
  <div class="step-band grey" style="left:98px;top:112px;width:124px"><strong>40%</strong><span>Lorem ipsum dolor sit amet, adipiscing elit, sed diam</span></div>
  <div class="step-band navy" style="left:70px;top:142px;width:152px"><strong>30%</strong><span>Lorem ipsum dolor sit amet, adipiscing elit, sed diam</span></div>
  <div class="step-band grey" style="left:42px;top:172px;width:180px"><strong>20%</strong><span>Lorem ipsum dolor sit amet, adipiscing elit, sed diam</span></div>
  <div class="legend" style="left:355px;top:75px"><i class="dot"></i>Lorem ipsum<p>Lorem ipsum dolor sit amet, consectetuer adipiscing elit, sed diam nonummy nibh euismod tincidunt ut laoreet</p></div>
  <div class="legend" style="left:355px;top:122px"><i class="dot g"></i>Lorem ipsum<p>Lorem ipsum dolor sit amet, consectetuer adipiscing elit, sed diam nonummy nibh euismod tincidunt ut laoreet</p></div>
  <div class="legend" style="left:355px;top:169px"><i class="dot"></i>Lorem ipsum<p>Lorem ipsum dolor sit amet, consectetuer adipiscing elit, sed diam nonummy nibh euismod tincidunt ut laoreet</p></div>
  <div class="legend" style="left:355px;top:216px"><i class="dot g"></i>Lorem ipsum<p>Lorem ipsum dolor sit amet, consectetuer adipiscing elit, sed diam nonummy nibh euismod tincidunt ut laoreet</p></div>
  <div class="foot-brand">Margin Loft</div><div class="page-num">18</div>
</section>

<!-- 19 Use cases -->
<section class="slide usecases" style="left:23px;top:1020px">
  <div style="left:28px;top:30px;width:60px;height:120px;border:3px solid #222;border-radius:8px;padding:28px 6px 6px;background:#fff">
    <div style="font-size:7px;color:var(--navy);font-weight:500;line-height:8px">Lorem ipsum dolor</div>
    <p style="font-size:3.6px;line-height:4.5px;color:#555;margin-top:22px">To introduce the students to the changing landscape of marketing and equip them with knowledge and tools.</p>
  </div>
  <div style="left:110px;top:70px;width:60px;height:120px;border:3px solid #222;border-radius:8px;padding:14px 6px 6px;background:#fff">
    <div style="font-size:7px;color:var(--navy);font-weight:500;line-height:8px">Dolor sit amet, conse</div>
    <p style="font-size:3.6px;line-height:4.5px;color:#555;margin-top:22px">You will learn concepts and ideas in digital marketing as well as how to use different tools and strategies.</p>
  </div>
  <div style="left:190px;top:112px;width:60px;height:120px;border:3px solid #222;border-radius:8px;padding:26px 6px 6px;background:#fff">
    <div style="font-size:7px;color:var(--navy);font-weight:500;line-height:8px;border-bottom:1px solid var(--navy)">Consec</div>
    <p style="font-size:3.6px;line-height:4.5px;color:#555;margin-top:20px">You are required to pass 80% of the evaluation test to obtain the certificate.</p>
  </div>
  <div class="ttl" style="left:275px;top:78px;font-size:30px">USE CASES</div>
  <p class="body" style="left:275px;top:120px;width:225px">Lorem ipsum dolor sit amet, consectetuer adipiscing elit, sed diam nonummy nibh euismod tincidunt ut laoreet dolore magna aliquam erat volutpat. Ut wisi enim ad minim veniam, quis nostrud exerci tation ullamcorper suscipit lobortis nisl ut aliquip ex ea commodo consequat. Duis autem vel eum iriure dolor in hendrerit i</p>
  <p class="body" style="left:275px;top:178px;width:225px">Lorem ipsum dolor sit amet, consectetuer adipiscing elit, sed diam nonummy nibh euismod tincidunt ut laoreet dolore magna aliquam erat volutpat. Ut wisi enim ad minim veniam, quis nostrud exerci tation ullamcorper suscipit lobortis nisl ut aliquip ex ea commodo consequat. Duis autem vel eum iriure dolor in hendrerit in</p>
  <div class="foot-brand">Margin Loft</div><div class="page-num">19</div>
</section>

<!-- 20 Team -->
<section class="slide team" style="left:312.5px;top:1020px">
  <div class="ttl" style="left:0;top:22px;width:515px;text-align:center;font-size:14px">TEAM MEMBERS <b>AND ADVISORS</b></div>
  <p class="body" style="left:85px;top:45px;width:345px;text-align:center">Lorem ipsum dolor sit amet, consectetuer adipiscing elit, sed diam nonummy nibh euismod tincidunt ut laoreet dolore magna aliquam erat volutpat. Ut wisi enim ad minim veniam, quis nostrud exerci tation ullamcorper suscipit lobortis nisl ut aliquip ex ea commodo consequat.</p>
  <p class="body" style="left:85px;top:78px;width:345px;text-align:center">Lorem ipsum dolor sit amet, cons ectetuer adipiscing elit, sed diam nonummy nibh euismod tincidunt ut laoreet dolore magna aliquam erat volutpat.</p>
  <div style="left:0;top:118px;width:515px;height:122px;background:var(--navy)"></div>
  <div style="left:0;top:124px;width:515px;display:grid;grid-template-columns:repeat(4,1fr);text-align:center;color:#fff;padding:0 10px">
    <div><div role="img" aria-label="Portrait of team member" style="width:46px;height:46px;border-radius:50%;background:linear-gradient(#c9d3e1,#8ea2bf);border:2px solid #fff;margin:0 auto"></div><div style="font-size:8.5px;font-weight:700;margin-top:8px">JONAH REED</div><p style="font-size:4.5px;line-height:5.5px;padding:2px 18px">Lorem ipsum dolor sit amet, cons ectetuer adipiscing elit, sed diam nonummy nibh euismod tincidunt ut laoreet dolore magna aliquam.</p></div>
    <div><div role="img" aria-label="Portrait of team member" style="width:46px;height:46px;border-radius:50%;background:linear-gradient(#c9d3e1,#8ea2bf);border:2px solid #fff;margin:0 auto"></div><div style="font-size:8.5px;font-weight:700;margin-top:8px">MILA HART</div><p style="font-size:4.5px;line-height:5.5px;padding:2px 18px">Lorem ipsum dolor sit amet, cons ectetuer adipiscing elit, sed diam nonummy nibh euismod tincidunt ut laoreet dolore magna aliquam.</p></div>
    <div><div role="img" aria-label="Portrait of team member" style="width:46px;height:46px;border-radius:50%;background:linear-gradient(#c9d3e1,#8ea2bf);border:2px solid #fff;margin:0 auto"></div><div style="font-size:8.5px;font-weight:700;margin-top:8px">JONAH REED</div><p style="font-size:4.5px;line-height:5.5px;padding:2px 18px">Lorem ipsum dolor sit amet, cons ectetuer adipiscing elit, sed diam nonummy nibh euismod tincidunt ut laoreet dolore magna aliquam.</p></div>
    <div><div role="img" aria-label="Portrait of team member" style="width:46px;height:46px;border-radius:50%;background:linear-gradient(#c9d3e1,#8ea2bf);border:2px solid #fff;margin:0 auto"></div><div style="font-size:8.5px;font-weight:700;margin-top:8px">MILA HART</div><p style="font-size:4.5px;line-height:5.5px;padding:2px 18px">Lorem ipsum dolor sit amet, cons ectetuer adipiscing elit, sed diam nonummy nibh euismod tincidunt ut laoreet dolore magna aliquam.</p></div>
  </div>
  <div class="foot-brand">Margin Loft</div><div class="page-num">20</div>
</section>

<!-- 21 Thank you -->
<section class="slide thanks" style="left:601px;top:1020px">
  <div class="photo" role="img" aria-label="Photo of business colleagues shaking hands in an office" style="left:230px;top:0;width:285px;height:289px;background:linear-gradient(90deg,#ffffff 0%,#dde3eb 30%,#a9b7ca 70%,#c4ceda 100%)"></div>
  <div class="brand-box" style="left:0;top:10px;width:235px;height:45px;font-size:27px">Margin Loft</div>
  <div class="ttl" style="left:20px;top:88px;font-size:27px;font-weight:800">Thank You</div>
  <div class="ttl" style="left:20px;top:138px;font-size:16px">CONTACT <b>US</b></div>
  <svg style="left:20px;top:160px" width="10" height="46" viewBox="0 0 10 46" fill="#0f3c78">
    <circle cx="5" cy="5" r="4.5"/><circle cx="5" cy="20" r="4.5"/><circle cx="5" cy="35" r="4.5"/>
    <path d="M3 3l1.2 0 .6 1.4-.7.6a4 4 0 0 0 1.9 1.9l.6-.7 1.4.6V8A5 5 0 0 1 3 3z" fill="#fff"/>
    <rect x="2.5" y="18" width="5" height="4" fill="#fff"/>
    <path d="M5 32a2 2 0 0 1 2 2c0 1.5-2 3.5-2 3.5S3 35.5 3 34a2 2 0 0 1 2-2z" fill="#fff"/>
  </svg>
  <div style="left:34px;top:159px;font-size:9.5px;line-height:15px;color:#444">555-014-2290<br>hello@marginloft-mail.com<br>12 Harbor Lane, Westford, box 40210</div>
  <div style="left:20px;top:230px;font-size:10px;letter-spacing:2px;font-weight:600;color:var(--navy)">www.marginloft-site.com</div>
  <div style="left:20px;top:250px"><i class="sq"></i><i class="sq"></i><i class="sq"></i><i class="sq"></i></div>
</section>

</body>
</html>
```